" Empresa de desenvolvimento humano, que trabalha principalmente a gestão dentro do ambiente de trabalho através de treinamento, consultoria e coaching. O principal conceito é que cada pessoa é única e seu auto-conhecimento é a chave para seu sucesso. "

```html
<!DOCTYPE html>
<html lang="pt-BR">
<head>
<meta charset="UTF-8">
<title>Título da Página</title>
<link href="https://fonts.googleapis.com/css2?family=Open+Sans:wght@400;600;800&display=swap" rel="stylesheet">
<style>
  :root {
    --page-grey: #e6e6e6;
    --slide-white: #ffffff;
    --brand-blue: #1a84d6;
    --brand-navy: #1d3a5c;
    --text-dark: #2b2b2b;
    --photo-light: #eef0f3;
    --photo-mid: #cfd5dc;
    --photo-deep: #9aa6b4;
  }
  * { margin: 0; padding: 0; box-sizing: border-box; }
  html, body { width: 1200px; height: 1200px; overflow: hidden; }
  body { background: var(--page-grey); font-family: "Open Sans", Arial, sans-serif; position: relative; }

  .slide { position: absolute; left: 0; top: 264px; width: 1200px; height: 684px; background: var(--slide-white); overflow: hidden; }

  .photo-team {
    position: absolute; left: 732px; top: 0; width: 468px; height: 684px;
    background: linear-gradient(180deg, var(--photo-mid) 0%, var(--photo-light) 35%, var(--photo-mid) 70%, var(--photo-deep) 100%);
  }

  .title-band { position: absolute; left: 72px; top: 89px; width: 864px; height: 58px; }
  .title-band svg { position: absolute; left: 0; top: -24px; overflow: visible; }
  .page-title {
    position: absolute; left: 19px; top: 0; line-height: 58px;
    color: #fff; font-weight: 800; font-size: 32px; letter-spacing: 0.3px;
  }

  .brand { position: absolute; left: 950px; top: 124px; display: flex; align-items: center; gap: 10px; }
  .brand-dot { width: 16px; height: 16px; border-radius: 50%; background: var(--brand-navy); }
  .brand-name { font-weight: 600; font-size: 36px; letter-spacing: 2px; color: var(--brand-navy); }

  .body-copy { position: absolute; left: 89px; top: 190px; width: 626px; color: var(--text-dark); font-size: 13.8px; line-height: 23px; text-align: justify; hyphens: auto; }
  .body-copy p + p { margin-top: 36px; }
</style>
</head>
<body>
  <section class="slide">
    <div class="photo-team" role="img" aria-label="Fotografia de uma equipe de colegas comemorando"></div>

    <div class="title-band">
      <svg width="864" height="110" viewBox="0 0 864 110">
        <polygon points="0,24 864,24 848,82 0,82" fill="var(--brand-blue)"/>
        <polygon points="666,0 768,0 762,10 660,10" fill="var(--brand-blue)"/>
        <polygon points="666,87 726,87 720,96 660,96" fill="var(--brand-blue)"/>
      </svg>
      <h1 class="page-title">TÍTULO DA PÁGINA</h1>
    </div>

    <div class="brand">
      <span class="brand-dot"></span>
      <span class="brand-name">INTEGRA</span>
    </div>

    <div class="body-copy">
      <p>Ao contrário do que se acredita, Lorem Ipsum não é simplesmente um texto randômico. Com mais de 2000 anos, suas raízes podem ser encontradas em uma obra de literatura latina clássica datada de 45 AC. Ricardo Almeida, um professor de latim do Colégio Vale Verde, pesquisou uma das mais obscuras palavras em latim, consectetur, oriunda de uma passagem de Lorem Ipsum, e, procurando por entre citações da palavra na literatura clássica, descobriu a sua indubitável origem. Lorem Ipsum vem das seções 1.10.32 e 1.10.33 do "de Finibus Bonorum et Malorum" (Os Extremos do Bem e do Mal), de Cícero, escrito em 45 AC. Este livro é um tratado de teoria da ética muito popular na época da Renascença. A primeira linha de Lorem Ipsum, "Lorem Ipsum dolor sit amet..." vem de uma linha na seção 1.10.32.</p>
      <p>O trecho padrão original de Lorem Ipsum, usado desde o século XVI, está reproduzido abaixo para os interessados. Seções 1.10.32 e 1.10.33 de "de Finibus Bonorum et Malorum" de Cícero também foram reproduzidas abaixo em sua forma exata original, acompanhada das versões para o inglês da tradução feita por H. Moreira em 1914.</p>
    </div>
  </section>
</body>
</html>
```